Circular Wedding Menu Design - Adobe Illustrator

I am looking for a design for circular wedding menus. these will be 7 inches.I'm providing a template from the printer, AI files of our wedding invitation, and the menu items.

The paper our invitations were printed on was a sandy beige color. please make the background for this the same color. It will be put ontop of a white plate with ivory tablecloth and cappucino covered napkins.

IMPORTANT - We aren't committed to a specific design so feel free to use whatever you like, but we definitely want the cow, fish, and carrot images from our rsvp to be used for the entrees in the menu.

IMPORTANT - must be in Adobe illustrator format

for inspiration:
http://cdn.plumbridalpages.example/wp-content/uploads/2012/10/harvel-styled-19.jpg

http://www.pictofind.example/imgres?imgurl=http%3A%2F%2Fwww.velvetknotstudio.example%2Fblog%2Fwp-content%2Fuploads%2F2013%2F07%2FRound-Menu-Wedding-Place-Setting.jpg&imgrefurl=http%3A%2F%2Fwww.velvetknotstudio.example%2Fblog%2Finspiration%2Fsimply-lovely-wedding-menu-place-settings%2F&h=815&w=600&zoom=1&page=1&start=0&ndsp=30

https://thumbs3.pictofind.example/images?q=tbn:Xk4mPq7RtL2vNw9HbYc3JdZs8FgQe1Ua

https://thumbs3.pictofind.example/images?q=tbn:Rb6wLn2TqZ8kVe4MhXs1PcYj9DuGa3Wo

https://thumbs2.pictofind.example/images?q=tbn:Hn5cWq8JtM3sLz7PxVb2KeRd6YgFo1Ni

```html
<!DOCTYPE html>
<html lang="en">
<head>
<meta charset="utf-8">
<title>Wedding Menu</title>
<link rel="stylesheet" href="https://fonts.googleapis.com/css2?family=Monsieur+La+Doulaise&family=Parisienne&family=Barlow+Semi+Condensed:wght@400;600&display=swap">
<style>
  :root {
    --paper: #ffffff;
    --ink: #1c1c1c;
    --gold: #b8922e;
    --vine: #d9d9d9;
    --vine-soft: rgba(205, 205, 205, 0);
    --icon: #111111;
  }
  * { margin: 0; padding: 0; box-sizing: border-box; }
  html, body {
    width: 1200px; height: 1159px; overflow: hidden;
    background: var(--paper);
  }
  .menu-card {
    position: relative;
    width: 1200px; height: 1159px;
    font-family: "Barlow Semi Condensed", "Arial Narrow", sans-serif;
    color: var(--ink);
  }
  .plate {
    position: absolute;
    left: 26px; top: 5px;
    width: 1148px; height: 1148px;
    border-radius: 50%;
    border: 1.5px solid var(--ink);
    background: var(--paper);
    overflow: hidden;
  }
  .vine {
    position: absolute;
    border-radius: 50%;
    background: radial-gradient(closest-side, var(--vine), var(--vine-soft));
    opacity: .75;
  }
  .vine--top    { left: 300px; top: -120px; width: 620px; height: 330px; }
  .vine--left   { left: -150px; top: 320px; width: 330px; height: 620px; }
  .vine--right  { left: 940px; top: 180px; width: 330px; height: 640px; }
  .vine--bottom { left: 200px; top: 930px; width: 720px; height: 320px; }

  .title {
    position: absolute;
    left: 330px; top: 50px; width: 570px;
    text-align: center;
    font-family: "Monsieur La Doulaise", "Parisienne", cursive;
    font-size: 230px; line-height: 1;
    color: var(--gold);
  }
  .course-label {
    position: absolute;
    font-family: "Parisienne", cursive;
    font-size: 54px; line-height: 1;
    color: var(--gold);
  }
  .rule {
    position: absolute;
    height: 1.5px;
    background: var(--gold);
  }
  .rule-dot {
    position: absolute;
    width: 13px; height: 13px;
    border-radius: 50%;
    border: 1.5px solid var(--gold);
    background: var(--paper);
  }
  .dish {
    position: absolute;
    font-size: 23px; line-height: 33px;
    letter-spacing: .2px;
  }
  .dish strong { font-weight: 600; }
  .dish-icon {
    position: absolute;
    background: var(--icon);
  }
</style>
</head>
<body>
<main class="menu-card">
  <div class="plate">
    <div class="vine vine--top" role="img" aria-label="Grey leafy vine pattern"></div>
    <div class="vine vine--left" role="img" aria-label="Grey leafy vine pattern"></div>
    <div class="vine vine--right" role="img" aria-label="Grey leafy vine pattern"></div>
    <div class="vine vine--bottom" role="img" aria-label="Grey leafy vine pattern"></div>
  </div>

  <h1 class="title">Menu</h1>

  <!-- Salad -->
  <h2 class="course-label" style="left:158px; top:310px;">Salad</h2>
  <span class="rule" style="left:330px; top:352px; width:818px;"></span>
  <span class="rule-dot" style="left:313px; top:346px;"></span>
  <div class="dish-icon" role="img" aria-label="Tomato icon" style="left:191px; top:383px; width:43px; height:46px; border-radius:50%;"></div>
  <p class="dish" style="left:246px; top:385px;"><strong>Grilled Watermelon &amp; Fig Salad:</strong> Gem Lettuces,<br>Watermelon, Figs, Toasted Hazelnuts, Balsamic<br>Reduction, Honey-Orange Dressing</p>

  <!-- Entrée -->
  <h2 class="course-label" style="left:398px; top:528px;">Entrée</h2>
  <span class="rule" style="left:23px; top:572px; width:340px;"></span>
  <span class="rule-dot" style="left:364px; top:566px;"></span>
  <div class="dish-icon" role="img" aria-label="Cow icon" style="left:402px; top:606px; width:78px; height:62px; border-radius:10px;"></div>
  <p class="dish" style="left:491px; top:606px;">Roasted Filet Mignon, Wild Mushrooms, Garlic Mashed<br>Potatoes, Asparagus with Red Wine Sauce</p>
  <div class="dish-icon" role="img" aria-label="Fish icon" style="left:410px; top:698px; width:73px; height:52px; border-radius:50%;"></div>
  <p class="dish" style="left:491px; top:687px;">Porcini Crusted Halibut, Lemon-Herb Potatoes, Black Kale,<br>Early Girl Tomatoes</p>
  <div class="dish-icon" role="img" aria-label="Carrot icon" style="left:420px; top:780px; width:52px; height:64px; border-radius:40% 40% 50% 10%;"></div>
  <p class="dish" style="left:491px; top:768px;">Artichoke Agnolotti, Wild Mushrooms, Baby Arugula, Goat<br>Cheese, White Wine Sauce, Micro Herbs</p>

  <!-- Wedding Cake -->
  <h2 class="course-label" style="left:609px; top:886px;">Wedding Cake</h2>
  <span class="rule" style="left:141px; top:937px; width:443px;"></span>
  <span class="rule-dot" style="left:584px; top:931px;"></span>
  <div class="dish-icon" role="img" aria-label="Cake slice icon" style="left:645px; top:972px; width:42px; height:51px; border-radius:6px 14px 2px 2px;"></div>
  <p class="dish" style="left:701px; top:965px;">Delicate Butter Pecan With<br>Fresh Raspberry Mouse</p>
</main>
</body>
</html>
```